Renewed electronic office supplies

I need a landing page design for a B2B business that will sell refurbished and renewed electronic devices such as smartphones, laptops, tablets and other gadgets. We want to become suppliers of these devices to companies that need computers and other devices for their employees. The point of our business is that they can get a great device that is in very good contrition instead of buying brand new. Companies will be able to save 50-60% on these renewed devices. Not only that we will also buy the companies old devices which they no longe needs and renew them and give them new life so we can resell it.

Our services will be:

- sale of renewed devices with lifetime warranty

- purchase of old devices

- swap solution: meaning client buy from us and sell at the same time so we deduct the amount sale of their old devices into their purchase.

Some useful information:

- company name and logo are still pending

- we aim to provide all business with top quality of renewed and environmentally friendly electronics, while maintaining a minimal impact on the natural environment.

I have attached a word document with some additional info that might be useful

Looking forward to seeing all your great designs!

P.s. Please feel free to make designs that are not based on my documents also, we need different layouts and designs. as for now I see many of the designs are more or less the same. we need more variation on design
Updates

Target Market(s)

Medium to large Businesses

Industry/Entity Type

Technology Equipment

Requirements
Must have
• we need more designs to be submitted , 50 designs minimum

```html
<!DOCTYPE html>
<html lang="en">
<head>
<meta charset="utf-8">
<title>Renewly – Reusable Electronic Office Supplies</title>
<link href="https://fonts.googleapis.com/css2?family=Roboto:wght@300;400;500;700;900&display=swap" rel="stylesheet">
<style>
:root{
  --hero-blue:#214a7d;
  --accent-green:#4cd68a;
  --deep-teal:#1e5e54;
  --footer-navy:#252a36;
  --ink:#1b1b1b;
  --muted:#5a5a5a;
  --white:#ffffff;
}
*{margin:0;padding:0;box-sizing:border-box}
html,body{width:1200px;height:2804px;overflow:hidden}
body{font-family:"Roboto",sans-serif;color:var(--ink);background:var(--white);position:relative}
.abs{position:absolute}

/* hero */
.hero{left:0;top:0;width:1200px;height:594px;background:var(--hero-blue);color:var(--white)}
.brand{left:158px;top:8px;font-weight:900;font-size:27px;line-height:30px;color:var(--white);letter-spacing:.5px}
.brand small{display:block;font-size:18px;line-height:20px}
.menu-icon{left:1021px;top:12px}
.hero-kicker{left:0;width:1200px;top:32px;text-align:center;font-size:35px;font-weight:400}
.hero-title{left:0;width:1200px;top:68px;text-align:center;font-size:58px;font-weight:700}
.hero-text{left:250px;width:700px;top:151px;text-align:center;font-size:17px;line-height:26px;font-weight:300}
.shop-btn{left:542px;top:245px;width:117px;height:35px;background:var(--accent-green);color:var(--white);font-weight:700;font-size:17px;display:flex;align-items:center;justify-content:center}
.hero-devices{left:201px;top:300px;width:850px;height:294px;border-radius:14px 14px 0 0;background:linear-gradient(180deg,#9aa6b4 0%,#5f7fa6 45%,#2c4f7c 100%)}

/* categories */
.cat-card{top:686px;width:210px;height:150px;border:1px solid #e4e4e4;padding:3px}
.cat-card .ph{width:100%;height:100%}
.cat-label{top:848px;width:210px;text-align:center;font-weight:500;font-size:16.5px;letter-spacing:.2px}

/* repair band */
.repair{left:0;top:942px;width:1200px;height:423px;background:var(--deep-teal);color:var(--white)}
.repair-intro{left:161px;top:50px;font-size:19.5px}
.repair-title{left:159px;top:82px;font-size:31px;line-height:39px;font-weight:700;width:470px;white-space:nowrap}
.repair-text{left:159px;top:209px;width:440px;font-size:16.5px;line-height:25px;white-space:nowrap}
.repair-photo{left:762px;top:27px;width:438px;height:396px;background:linear-gradient(135deg,#2a6a60 0%,#1a1a1a 45%,#3c3c3c 70%,#d8b8a6 100%)}

/* feature rows */
.feature-title{font-size:43px;font-weight:700;color:var(--ink)}
.feature-text{width:460px;font-size:16.5px;line-height:25px;color:var(--muted);white-space:nowrap}
.buy-photo{left:632px;top:1388px;width:568px;height:519px;background:linear-gradient(135deg,#d9dcdf 0%,#3fc5e2 45%,#35bcd9 100%)}
.sell-photo{left:0;top:1930px;width:566px;height:518px;background:linear-gradient(135deg,#e8d2b0 0%,#5ca4d6 40%,#ececec 75%,#f5f5f5 100%)}

/* footer */
.footer{left:0;top:2467px;width:1200px;height:337px;background:var(--footer-navy);color:var(--white)}
.footer-brand{left:158px;top:100px;font-weight:900;font-size:34px;line-height:38px}
.footer-brand small{display:block;font-size:21px;line-height:24px}
.footer-heading{top:72px;font-size:22px;font-weight:400}
.contact-list{left:383px;top:114px;list-style:none;font-size:15px}
.contact-list li{display:flex;align-items:flex-start;gap:9px;height:31.5px}
.contact-list svg{flex:none;margin-top:2px}
.newsletter-sub{left:723px;top:113px;font-size:16.5px}
.newsletter-form{left:723px;top:144px;display:flex}
.email-field{width:226px;height:43px;background:var(--white);color:#666;font-size:13.5px;display:flex;align-items:center;padding-left:17px}
.go-btn{width:93px;height:43px;background:var(--accent-green);color:var(--white);font-size:16px;display:flex;align-items:center;justify-content:center}
.copyright{left:723px;top:212px;font-size:12px}
</style>
</head>
<body>

<header class="hero abs">
  <div class="brand abs">RENEWLY<small>SUPPLY</small></div>
  <svg class="menu-icon abs" width="22" height="18" viewBox="0 0 22 18"><rect y="1" width="22" height="3" fill="#fff"/><rect y="7.5" width="22" height="3" fill="#fff"/><rect y="14" width="22" height="3" fill="#fff"/></svg>
  <div class="hero-kicker abs">Reusable Electronic</div>
  <h1 class="hero-title abs">Office Supplies</h1>
  <p class="hero-text abs">we aim to provide all business with top quality of reused<br>and environmentally friendly electronics, while maintaining a minimal impact on<br>the natural environment.</p>
  <div class="shop-btn abs">SHOP</div>
  <div class="hero-devices abs" role="img" aria-label="Row of refurbished smartphones showing their home screens"></div>
</header>

<section class="categories">
  <div class="cat-card abs" style="left:158px"><div class="ph" role="img" aria-label="Hand holding a smartphone above a keyboard" style="background:linear-gradient(135deg,#c9c2bb,#e26a8d 55%,#dfe3ea)"></div></div>
  <div class="cat-label abs" style="left:158px">SMARTPHONES</div>
  <div class="cat-card abs" style="left:382px"><div class="ph" role="img" aria-label="Person typing on a laptop" style="background:linear-gradient(135deg,#dcdcdc,#6d8fb8 55%,#9a9a9a)"></div></div>
  <div class="cat-label abs" style="left:382px">LAPTOPS</div>
  <div class="cat-card abs" style="left:608px"><div class="ph" role="img" aria-label="Two tablets with keyboards on a pink desk" style="background:linear-gradient(180deg,#a9d1d4,#c78384 60%,#3a3a3a)"></div></div>
  <div class="cat-label abs" style="left:608px">TABLETS</div>
  <div class="cat-card abs" style="left:832px"><div class="ph" role="img" aria-label="Tablets, phones and a smartwatch laid flat" style="background:linear-gradient(135deg,#f2f2f2,#8fb6e6 50%,#e7a4c4)"></div></div>
  <div class="cat-label abs" style="left:832px">GADGETS</div>
</section>

<section class="repair abs">
  <div class="repair-intro abs">We are</div>
  <h2 class="repair-title abs">AFFORDABLE MOBILE<br>PHONE &amp; TABLET<br>DEVICE REPAIR SHOP</h2>
  <p class="repair-text abs">Many desktop publishing packages and web page editors<br>now use Lorem Ipsum as their default model text, and a<br>search for ‘lorem ipsum’ will uncover many web sites.<br>During the meeting you will receive plenty of information<br>concerning the most effective solutions for personal and<br>property protection.</p>
  <div class="repair-photo abs" role="img" aria-label="Hand holding a smartphone with a cracked screen"></div>
</section>

<section class="feature-buy">
  <h2 class="feature-title abs" style="left:159px;top:1550px">Buy Reusable IT</h2>
  <p class="feature-text abs" style="left:159px;top:1618px">We specialize in refurbished electronic devices with top<br>quality for affordable prices. All our products have<br>undergone a detailed testing and reconditioning program by<br>expert technicians.</p>
  <div class="buy-photo abs" role="img" aria-label="Laptop, tablet, phone, pencil and earbuds on a blue surface"></div>
</section>

<section class="feature-sell">
  <div class="sell-photo abs" role="img" aria-label="Phone, tablet and keyboard on a marble desk"></div>
  <h2 class="feature-title abs" style="left:604px;top:2101px">Sell your IT Safely</h2>
  <p class="feature-text abs" style="left:604px;top:2169px">We can also buy your used electronics and make sure they<br>get reused and give them a new life. By selling your used<br>devices that you no longer have use for you can help us<br>create carbon savings.</p>
</section>

<footer class="footer abs">
  <div class="footer-brand abs">RENEWLY<small>SUPPLY</small></div>

  <h3 class="footer-heading abs" style="left:383px">GET IN TOUCH</h3>
  <ul class="contact-list abs">
    <li><svg width="14" height="14" viewBox="0 0 24 24"><path fill="#fff" d="M6.6 10.8a15.5 15.5 0 0 0 6.6 6.6l2.2-2.2c.3-.3.7-.4 1-.2 1.1.4 2.3.6 3.6.6.6 0 1 .4 1 1V20c0 .6-.4 1-1 1A17 17 0 0 1 3 4c0-.6.4-1 1-1h3.5c.6 0 1 .4 1 1 0 1.3.2 2.5.6 3.6.1.3 0 .7-.2 1z"/></svg>Phone : 1 300 555 417</li>
    <li><svg width="14" height="14" viewBox="0 0 24 24"><path fill="#fff" d="M6 2h9l3 3v5h2a2 2 0 0 1 2 2v10H2V12a2 2 0 0 1 2-2h2zm2 2v6h8V6h-2V4zM6 14v2h3v-2zm0 4v2h3v-2zm5-4v2h7v-2zm0 4v2h7v-2z"/></svg>Fax : +61 3 9000 4128</li>
    <li><svg width="14" height="14" viewBox="0 0 24 24"><path fill="#fff" d="M2 5h20v14H2zm2 2v.5l8 5 8-5V7zm0 3v7h16v-7l-8 5z"/></svg>Email : hello@renewly.example</li>
    <li><svg width="14" height="16" viewBox="0 0 24 28"><path fill="#fff" d="M12 1a9 9 0 0 0-9 9c0 7 9 17 9 17s9-10 9-17a9 9 0 0 0-9-9zm0 12.5A3.5 3.5 0 1 1 12 6.5a3.5 3.5 0 0 1 0 7z"/></svg><span>Location : 45 Harbour Lane, Carlton<br><span style="padding-left:71px">3053 Australia</span></span></li>
  </ul>

  <h3 class="footer-heading abs" style="left:723px">NEWSLETTER</h3>
  <div class="newsletter-sub abs">Sign up your newsletter</div>
  <div class="newsletter-form abs">
    <div class="email-field">Email Adress</div>
    <div class="go-btn">GO</div>
  </div>
  <div class="copyright abs">Copyright © 2020 renewly. All Rights Reserved</div>
</footer>

</body>
</html>
```